Handyman Business Card and website logo design

I need a logo for my new handyman business. The logo will be used for my website, business cards, and Facebook pages. I want my business card to have this logo and have a simplistic and nicely flowing design with a handyman feel.

The name of my business is Quillbrook (Dr is for doctor NOT Drive). So my thoughts for my logo is a handyman with a stethoscope and looking like a doctor examining a house. With handyman will have a tool-belt on and holding a drill or some other well recognized tool. Basically a handyman doctor examining someones "precious home" so that he can prescribe the right "fix" for them.

Martin Pellworth (CEO)
KTNestFixer
4137 Wyndmoor Court
Alderbrook, MN 60391

```html
<!DOCTYPE html>
<html lang="en">
<head>
<meta charset="UTF-8">
<title>Quillbrook – Business Card</title>
<link rel="stylesheet" href="https://fonts.googleapis.com/css2?family=Source+Sans+3:wght@400;600;700&display=swap">
<style>
  :root {
    --stage: #1c1c1c;
    --card-white: #ffffff;
    --brand-blue: #1170b9;
    --text-grey: #5a5a5a;
    --on-blue: #ffffff;
  }
  html, body {
    margin: 0;
    padding: 0;
    width: 1200px;
    height: 900px;
    overflow: hidden;
    background: var(--stage);
    font-family: "Source Sans 3", "Myriad Pro", Arial, sans-serif;
  }
  .canvas {
    position: relative;
    width: 1200px;
    height: 900px;
  }
  .card {
    position: absolute;
    top: 170px;
    width: 347px;
    height: 561px;
    box-sizing: border-box;
  }
  .card-front {
    left: 259px;
    background: var(--card-white);
  }
  .card-back {
    left: 631px;
    background: var(--brand-blue);
  }
  .accent-tab {
    position: absolute;
    left: 102px;
    width: 143px;
    height: 30px;
    background: var(--brand-blue);
  }
  .accent-tab.top { top: 0; }
  .accent-tab.bottom { bottom: 0; height: 28px; }

  .brand-name {
    position: absolute;
    left: 0;
    right: 0;
    text-align: center;
    font-weight: 700;
    font-size: 48px;
    line-height: 1;
    letter-spacing: 0.5px;
    white-space: nowrap;
  }
  .card-front .brand-name {
    top: 188px;
    color: var(--brand-blue);
  }
  .card-back .brand-name {
    top: 258px;
    color: var(--on-blue);
  }

  .contact {
    position: absolute;
    top: 321px;
    left: 0;
    right: 0;
    text-align: center;
  }
  .contact-name {
    margin: 0;
    color: var(--brand-blue);
    font-weight: 700;
    font-size: 20px;
    line-height: 24px;
  }
  .contact-role {
    margin: 0 0 16px;
    color: var(--text-grey);
    font-size: 15px;
    line-height: 22px;
  }
  .contact-address {
    margin: 0;
    color: var(--text-grey);
    font-size: 16.5px;
    line-height: 20px;
    font-style: normal;
  }
</style>
</head>
<body>
<main class="canvas">
  <section class="card card-front">
    <div class="accent-tab top"></div>
    <div class="brand-name">Quillbrook</div>
    <div class="contact">
      <p class="contact-name">Martin Pellworth</p>
      <p class="contact-role">CEO</p>
      <address class="contact-address">4137 Wyndmoor Court<br>Alderbrook, MN 60391</address>
    </div>
    <div class="accent-tab bottom"></div>
  </section>

  <section class="card card-back">
    <div class="brand-name">Quillbrook</div>
  </section>
</main>
</body>
</html>
```